Text only wordpress site to capture emails

Refer to inspiration upload for list of sites that will be useful for you.

We need a site that will be used to capture emails from clients that follow us on social media. The site will be all text, pretty simple. I have a couple of text sites that I like and we can use them for an example.

Menu section will have home, archive, about.
Footer will have © and Website Privacy Policy | Legal and Policies
There will be some text on the home page and an email capture.

This site will be all text no pictures.

I discuss Cubicle Matters so the text portions will have some questions and answers on this and then prompt for the visitor to subscribe to my email list.

The only purpose of the site is to build an email list from existing social media followers so the site will be pretty simple in and of itself.

• Text only, similar Q&A to uploaded pics.

I will use a template from mail lantern dotcom for email capture.

I like the simple couriernew font family that is on both sites supplied in the uploads.
• If you use any color it needs to be very minimal.

```html
<!DOCTYPE html>
<html lang="en">
<head>
<meta charset="utf-8">
<title>Cubicle Matters</title>
<link rel="stylesheet" href="https://fonts.googleapis.com/css2?family=Courier+Prime:wght@400;700&display=swap">
<style>
  :root {
    --ink: #111111;
    --text: #333333;
    --muted: #8a8a8a;
    --rule: #cfcfcf;
    --field-border: #dddddd;
    --button: #cccccc;
    --paper: #ffffff;
  }
  * { box-sizing: border-box; margin: 0; padding: 0; }
  html, body {
    width: 1200px; height: 613px; overflow: hidden;
    background: var(--paper);
    font-family: "Courier Prime", "Courier New", monospace;
    color: var(--text);
  }
  .wrap { width: 876px; margin: 0 auto; position: relative; }

  .site-header { height: 78px; border-bottom: 1px dashed var(--rule); }
  .site-header .wrap { display: flex; justify-content: space-between; align-items: center; height: 78px; }
  .brand { font-size: 30px; font-weight: 700; color: var(--ink); letter-spacing: 0.5px; margin-top: -4px; }
  .main-nav { display: flex; gap: 54px; margin-top: 4px; }
  .main-nav a { font-size: 15px; color: var(--ink); text-decoration: none; }

  .content { height: 410px; }
  .content .wrap { display: flex; padding-top: 48px; }
  .newsletter { width: 266px; margin-right: 48px; }
  .section-title { font-size: 25px; font-weight: 700; color: var(--text); margin-bottom: 12px; letter-spacing: 0.3px; }
  .newsletter p { font-size: 14px; line-height: 23px; color: var(--muted); margin-bottom: 19px; }
  .email-field {
    display: block; width: 265px; height: 37px; margin-left: -2px;
    border: 1px solid var(--field-border); border-radius: 3px;
    box-shadow: 0 1px 3px rgba(0,0,0,0.08);
    font-family: inherit; font-size: 13.5px; padding: 0 12px; color: var(--muted);
    background: var(--paper);
  }
  .email-field::placeholder { color: var(--muted); }
  .subscribe {
    display: block; margin: 23px 0 0 -2px; width: 137px; height: 35px;
    background: var(--button); border: none; border-radius: 2px;
    box-shadow: 0 2px 3px rgba(0,0,0,0.12);
    font-family: inherit; font-size: 15px; font-weight: 700; color: var(--text);
    padding-top: 6px;
  }
  .about { flex: 1; }
  .about p { font-size: 13.5px; line-height: 22px; color: var(--text); margin-bottom: 19px; }
  .about strong { color: var(--ink); }

  .site-footer { border-top: 1px dashed var(--rule); }
  .site-footer .wrap { display: flex; justify-content: space-between; padding-top: 31px; }
  .legal p { font-size: 13.5px; line-height: 29px; color: var(--text); }
  .social { display: flex; align-items: center; gap: 12px; margin-top: 3px; margin-right: -4px; }
  .social-label { font-size: 13.5px; color: var(--text); margin-right: 2px; }
  .social-link {
    width: 37px; height: 37px; border-radius: 50%;
    border: 1px solid #e6e6e6; box-shadow: 0 1px 2px rgba(0,0,0,0.08);
    display: flex; align-items: center; justify-content: center;
    font-size: 11px; font-weight: 700; color: var(--text); text-decoration: none;
  }
</style>
</head>
<body>
  <header class="site-header">
    <div class="wrap">
      <div class="brand">Cubicle Matters</div>
      <nav class="main-nav">
        <a href="#">Home</a>
        <a href="#">Archive</a>
        <a href="#">About</a>
      </nav>
    </div>
  </header>

  <main class="content">
    <div class="wrap">
      <section class="newsletter">
        <h2 class="section-title">Newsletter</h2>
        <p>Lorem ipsum dolor sit ametere consectetuer adipiscing eoier eliter sederer diame nonummye nibh euismod tinci laor</p>
        <input class="email-field" type="email" placeholder="Email Here">
        <button class="subscribe" type="button">Subscribe</button>
      </section>
      <section class="about">
        <h2 class="section-title">About Us</h2>
        <p>Lorem ipsum dolor sit amet, consectetuer adipiscing elit, sed diam nonummy nibh euismod tincidunt ut laoreet dolore magna aliquam erat volutpat. Ut wisi enim ad minim veniam, quis nostrud exerci tation ullamcorper suscipit lobortis nisl ut aliquip ex ea codo consequat. Duis autem vel eum iriure dolor in hendrerit quis magna?</p>
        <p>To send us politics: <strong>info@cubiclematters.com</strong></p>
        <p>To talk to us ipsum dolor sit amet consectetuer:<br><strong>info@cubiclematters.com</strong></p>
        <p>Need to send us a legal letter? <strong>Please don’t.</strong></p>
      </section>
    </div>
  </main>

  <footer class="site-footer">
    <div class="wrap">
      <div class="legal">
        <p>Copyright © 2021 Cubicle Matters. All Rights Reserved.</p>
        <p>Privacy Policy | Legal and Policies</p>
      </div>
      <div class="social">
        <span class="social-label">Follow Us:</span>
        <a class="social-link" href="#">Pals</a>
        <a class="social-link" href="#">Peep</a>
      </div>
    </div>
  </footer>
</body>
</html>
```